Maple Home Health Care of San Diego needs a brochure to advertise its services.

We need a brochure for a new company called Maple Home Health Care of San Diego, Inc. We provide skilled home health care services such as skilled nursing, physical, occupational, and speech therapy, medical social work, and home health aide services. Our patient population is mostly 65 years and older. We market our services in the community, including hospitals, skilled nursing and assisted living facilities, doctor's offices etc. We would like to see designs that are easy to read, go with our logo color, which is green, and includes pictures of multicultural elderly individuals receiving medical or rehab care in or surrounding the home. Please include the information contained in the files attached, which has our services, about home health care, and our mission and vision.
Maple Home Health Care of San Diego, Inc.
4827 Harbor Crest Lane, Suite 5B
Encinitas, CA 92031
760-418-LEAF (office)
76- 529-LEAF (fax)
760-284-5370 (cell)

Target Market(s)

See above

Industry/Entity Type

Home Health Care

Font styles to use
Sans Serif

Colors
9bcb3c
add136

Requirements
Must have
• Must be tri-fold and geared toward an elderly and medical field population. Please view some other home health agency brochures out there for examples.

```html
<!DOCTYPE html>
<html lang="en">
<head>
<meta charset="utf-8">
<title>Maple Home Health Care of San Diego – Tri-fold Brochure</title>
<link href="https://fonts.googleapis.com/css2?family=Oswald:wght@300;400;500;600&family=Open+Sans:wght@400;600;700&display=swap" rel="stylesheet">
<style>
  :root{
    --green:#52b947;
    --green-dark:#2f8f3a;
    --green-light:#9bcb3c;
    --grey:#6d6e71;
    --grey-dark:#4d4e50;
    --grey-light:#a7a9ac;
    --text:#58595b;
    --paper:#ffffff;
    --backdrop:#dcddde;
  }
  *{box-sizing:border-box;margin:0;padding:0}
  html,body{width:934px;height:1200px;overflow:hidden}
  body{background:var(--backdrop);font-family:"Open Sans",Arial,sans-serif;color:var(--text);position:relative}

  .spread{position:absolute;left:37px;width:860px;height:560px;background:var(--paper);display:flex;box-shadow:0 2px 10px rgba(0,0,0,.12)}
  .spread--outside{top:30px}
  .spread--inside{top:620px}
  .panel{position:relative;width:286.67px;height:100%;overflow:hidden;flex:none}
  .panel + .panel{border-left:1px solid #eeeeee}

  .photo{display:block;width:100%}

  /* ---------- Outside: mission/vision flap ---------- */
  .mission-intro{height:125px;padding:18px 18px 0;color:var(--green);font-size:11.6px;font-weight:600;line-height:1.5}
  .photo--cards{height:165px;background:linear-gradient(135deg,#e9dcc6 0%,#c9a985 45%,#8c7a6b 100%)}
  .vision{height:270px;display:flex}
  .side-tab{width:34px;flex:none;display:flex;align-items:center;justify-content:center}
  .side-tab span{writing-mode:vertical-rl;transform:rotate(180deg);font-family:"Oswald",Arial,sans-serif;font-size:18px;color:#fff;font-weight:400;letter-spacing:.3px}
  .side-tab--green{background:var(--green)}
  .side-tab--grey{background:var(--grey)}
  .vision-body{flex:1;background:var(--grey);color:#fff;font-size:9.8px;line-height:1.45;padding:14px 14px 0}
  .vision-body p + p{margin-top:10px}

  /* ---------- Outside: contact panel ---------- */
  .photo-frame{position:relative;height:330px;display:flex}
  .photo--senior{flex:1;height:100%;background:linear-gradient(160deg,#f1ece4 0%,#d8c2a6 50%,#a89179 100%)}
  .photo-frame .side-tab{height:100%}
  .rule-green{height:4px;background:var(--green)}
  .contact{padding:18px 22px 0;text-align:center}
  .brand-name{font-family:"Oswald",Arial,sans-serif;font-weight:400;color:var(--green);text-align:center;line-height:1.25}
  .brand-name--small{font-size:13px}
  .address{margin-top:8px;font-family:"Oswald",Arial,sans-serif;font-weight:300;font-size:14.5px;line-height:1.4;color:var(--grey-dark)}
  .address .company{color:var(--green)}
  .divider{height:1px;background:var(--grey-light);margin:10px 0 8px}
  .contact-list{list-style:none;text-align:left;font-family:"Oswald",Arial,sans-serif;font-weight:300;font-size:14px;line-height:1.45;color:var(--grey-dark)}
  .contact-list .label{display:inline-block;width:48px}
  .contact-list .value{color:var(--green)}

  /* ---------- Outside: cover ---------- */
  .photo--cover{height:330px;background:linear-gradient(150deg,#f3eee6 0%,#e2d2bd 45%,#b9a48c 100%)}
  .cover-rule{height:3px;background:var(--green)}
  .cover-body{padding:28px 20px 0;text-align:center}
  .brand-name--cover{font-size:17px;color:var(--grey-dark)}
  .tagline{margin-top:22px;font-family:"Oswald",Arial,sans-serif;line-height:1.2}
  .tagline-line1{display:block;color:var(--green);font-size:20px;font-weight:500}
  .tagline-line2{display:block;color:var(--grey-dark);font-size:24px;font-weight:400}
  .website{margin-top:20px;color:var(--green);font-weight:700;font-size:12px}

  /* ---------- Inside: about ---------- */
  .about-hero{position:relative;height:120px}
  .photo--care{position:absolute;inset:0;background:linear-gradient(135deg,#cdb79b 0%,#8a6b55 55%,#c9c3bb 100%)}
  .about-hero svg{position:absolute;left:0;top:0}
  .about{padding:8px 16px 0}
  .about h2{font-family:"Oswald",Arial,sans-serif;font-weight:600;font-size:20px;line-height:1.1;color:var(--grey-dark)}
  .about h2 .accent{display:block;color:var(--green);font-size:22px}
  .about p{font-size:9.4px;line-height:1.42;margin-top:7px}
  .compliance{margin:9px 16px 0;border:1px solid var(--grey-light);border-radius:8px;padding:6px 8px;font-size:6.8px;line-height:1.4}

  /* ---------- Inside: services ---------- */
  .services{position:relative;width:573.33px;height:100%;flex:none;border-left:1px solid #eeeeee}
  .services-header{height:34px;background:var(--grey);color:#fff;font-weight:700;font-size:12.5px;display:flex;align-items:center;padding-left:18px}
  .services-cols{display:flex;height:526px}
  .services-col{width:50%;padding:10px 18px 0;position:relative}
  .services-col + .services-col{border-left:1px solid #eeeeee}
  .service + .service{margin-top:10px}
  .service h3{font-family:"Oswald",Arial,sans-serif;font-size:17px;font-weight:500;color:var(--green);line-height:1.2}
  .service h3 .lead{color:var(--green-dark);font-weight:600}
  .service ul{list-style:none;margin-top:3px;border-top:1px solid #dddddd;padding-top:3px}
  .service li{font-size:9.4px;line-height:1.38;padding-left:8px;text-indent:-8px}
  .service li::before{content:"- "}
  .photo--aide{position:absolute;left:0;bottom:0;width:100%;height:175px;background:linear-gradient(135deg,#efe9e0 0%,#d6c7b4 50%,#b8c3c7 100%)}

  .footer-band{position:absolute;left:0;bottom:0;width:573.33px;height:46px;background:var(--green);display:flex;align-items:center;padding-left:302px;color:#fff}
  .footer-band strong{font-family:"Oswald",Arial,sans-serif;font-weight:500;font-size:24px;margin-right:6px}
  .footer-band span{font-size:11px}
</style>
</head>
<body>

<section class="spread spread--outside" aria-label="Brochure outside">
  <article class="panel panel--mission">
    <p class="mission-intro">Our mission is to provide high quality, multi-disciplinary care by competent, caring and well-trained professionals who are responsive to the needs of our patients, their families and the communities we serve.</p>
    <div class="photo photo--cards" role="img" aria-label="Photo of a smiling senior couple playing cards at home"></div>
    <div class="vision">
      <div class="side-tab side-tab--green"><span>Our Vision</span></div>
      <div class="vision-body">
        <p>To be the provider of choice for quality home health care services, recognized for enduring dedication to provide innovative, professional, and compassionate care to the community we serve.</p>
        <p>To be one of the leading employers for healthcare professionals by providing our staff with an inviting work environment, competitive compensation and knowledgeable, trustworthy management and direction.</p>
        <p>To satisfy our patients’ needs and exceed their expectations by utilizing best practices and quality care standards.</p>
      </div>
    </div>
  </article>

  <article class="panel panel--contact">
    <div class="photo-frame">
      <div class="photo photo--senior" role="img" aria-label="Photo of a smiling senior man with glasses"></div>
      <div class="side-tab side-tab--grey"><span>Our Mission</span></div>
    </div>
    <div class="rule-green"></div>
    <div class="contact">
      <p class="address">
        <span class="company">Maple Home Health Care of San Diego, Inc.</span><br>
        4827 Harbor Crest Lane, Suite 5B<br>
        Encinitas, CA 92031
      </p>
      <div class="divider"></div>
      <ul class="contact-list">
        <li><span class="label">Phone:</span><span class="value">760-418-LEAF</span></li>
        <li><span class="label">Fax:</span><span class="value">76- 529-LEAF</span></li>
        <li><span class="label">Email:</span><span class="value">hello@cedarwellnurses.org</span></li>
      </ul>
    </div>
  </article>

  <article class="panel panel--cover">
    <div class="photo photo--cover" role="img" aria-label="Photo of a caregiver smiling with a senior man at home"></div>
    <div class="cover-rule"></div>
    <div class="cover-body">
      <p class="brand-name brand-name--cover">Maple Home Health Care of San Diego</p>
      <h1 class="tagline">
        <span class="tagline-line1">Making a tangible difference</span>
        <span class="tagline-line2">in your health at home</span>
      </h1>
      <p class="website">www.cedarwellnurses.org</p>
    </div>
  </article>
</section>

<section class="spread spread--inside" aria-label="Brochure inside">
  <article class="panel panel--about">
    <div class="about-hero">
      <div class="photo photo--care" role="img" aria-label="Photo of a nurse checking on a senior man seated at home"></div>
      <svg width="287" height="120" viewBox="0 0 287 120" aria-hidden="true">
        <polygon points="0,70 150,120 0,120" fill="#ffffff"/>
        <polygon points="0,58 180,120 150,120 0,70" fill="#52b947"/>
      </svg>
    </div>
    <div class="about">
      <h2>What is <span class="accent">home health care?</span></h2>
      <p>Home health care provides skilled nursing care, physical therapy, occupational therapy, speech therapy, and medical social services delivered in the comfort of your own home. This care may be provided for an injury, illness, or after a surgical procedure, with the goal of helping you recover, regain your independence and empowering you to reach and keep your best physical, mental, and social well-being.</p>
      <p>Home health care is ordered by your doctor. Our home health care professionals work with you and your doctor to evaluate your health care needs and establish a plan of care to provide services to meet those needs. Home health care is usually less expensive, more convenient, and having care provided at home is most often preferred.</p>
    </div>
    <p class="compliance">In compliance with Title VI of the Civil Rights Act of 1964, with Section 504 of the Rehabilitation Act of 1973 and with the Age Discrimination Act of 1975, Maple Home Health Care of San Diego does not discriminate on the basis of race, color, gender/national origin, age or disability with regard to admission, access to treatment or employment. We will make every effort to comply with these and similar statutes.</p>
  </article>

  <div class="services">
    <h2 class="services-header">We provide the following services in the comfort of your home:</h2>
    <div class="services-cols">
      <div class="services-col">
        <section class="service">
          <h3><span class="lead">Skilled</span> Nursing</h3>
          <ul>
            <li>Assess for changes in medical condition</li>
            <li>Education regarding disease management</li>
            <li>Teach how to manage and administer medication</li>
            <li>Perform medical procedures such as catheter insertion, wound care, ostomy care, lab work and injections</li>
          </ul>
        </section>
        <section class="service">
          <h3><span class="lead">Physical</span> Therapy</h3>
          <ul>
            <li>Focus on exercises and activities to improve balance, strength, and endurance, to reduce the risk of falls</li>
            <li>Improve ability to ambulate and/or transfer</li>
            <li>Evaluate the need for and train in the use of devices such as walker, cane, wheelchair</li>
            <li>Instruct in home exercise program</li>
          </ul>
        </section>
        <section class="service">
          <h3><span class="lead">Occupational</span> Therapy</h3>
          <ul>
            <li>Focus on the ability to perform activities of daily living such as bathing, dressing, and household tasks</li>
            <li>Evaluate the need for and train in the use of adaptive equipment to aid in performing activities of daily living</li>
            <li>Teach energy conservation techniques</li>
            <li>Instruct in home exercise program</li>
          </ul>
        </section>
      </div>
      <div class="services-col">
        <section class="service">
          <h3><span class="lead">Speech</span> Therapy</h3>
          <ul>
            <li>Improve communication skills</li>
            <li>Focus on the ability to swallow safely</li>
            <li>Improve memory and cognition/thinking skills</li>
          </ul>
        </section>
        <section class="service">
          <h3><span class="lead">Medical</span> Social Work</h3>
          <ul>
            <li>Provide referrals to community resources</li>
            <li>Provide short-term counseling for patients and caregivers</li>
            <li>Assist with living arrangements, financial concerns, and long-term planning</li>
            <li>Focus on overall social and emotional health</li>
          </ul>
        </section>
        <section class="service">
          <h3><span class="lead">Home</span> Health Aide</h3>
          <ul>
            <li>Provided when you are receiving skilled nursing, physical, occupational, or speech therapy</li>
            <li>Help with personal care on a short-term basis, such as bathing, dressing, toileting, light meal prep</li>
          </ul>
        </section>
        <div class="photo photo--aide" role="img" aria-label="Photo of a young nurse holding hands with a senior woman"></div>
      </div>
    </div>
  </div>

  <div class="footer-band"><strong>Your health</strong><span>is our primary concern</span></div>
</section>

</body>
</html>
```